Velkaros Pendants

Brightmoor Studio is a growing wedding ring wholesaler/manufacturer based in NYC. We have recently teamed up with a cross designer from Greece and added their line of cross pendants to our product line. We would like to introduce the product to our customers. We are looking for a clean looking postcard. Is it possible to remove the style number and weights from the bottom right corner of each image?
We will provide wording, etc. upon request.

Thanks.
Updates

We would like all or most images to be on the postcard, front and back is fine. Thanks!!

Industry/Entity Type

Wedding

```html
<!DOCTYPE html>
<html lang="en">
<head>
<meta charset="UTF-8">
<title>Velkaros Pendants – Postcard</title>
<link rel="stylesheet" href="https://fonts.googleapis.com/css2?family=Great+Vibes&family=Lato:wght@400&display=swap">
<style>
  :root {
    --wine-deep: #5a1332;
    --wine: #7a1d44;
    --wine-light: #9b2a57;
    --gold: #e2bb52;
    --gold-light: #f7e39a;
    --gold-dark: #b88a2a;
    --text-gold: #f2cf8e;
    --white: #ffffff;
    --backdrop: #1c1c1c;
  }
  * { margin: 0; padding: 0; box-sizing: border-box; }
  html, body { width: 1200px; height: 900px; overflow: hidden; background: var(--backdrop); }
  .postcard {
    position: relative;
    width: 1200px;
    height: 900px;
    overflow: hidden;
    background:
      radial-gradient(ellipse 700px 500px at 900px 250px, var(--wine-light), transparent 70%),
      linear-gradient(160deg, var(--wine) 0%, var(--wine) 50%, var(--wine-deep) 100%);
    font-family: "Lato", sans-serif;
  }
  .shapes { position: absolute; inset: 0; }
  .ornament {
    position: absolute;
    border-radius: 50%;
    background: radial-gradient(circle, rgba(247, 227, 154, 0.55), rgba(226, 187, 82, 0.2) 55%, transparent 75%);
  }
  .ornament--top-left { left: 40px; top: 0; width: 560px; height: 300px; }
  .ornament--bottom-left { left: 60px; top: 700px; width: 560px; height: 220px; }
  .ornament--top-right { right: -40px; top: -40px; width: 300px; height: 300px; }
  .ornament--bottom-right { right: -30px; bottom: -40px; width: 300px; height: 240px; }
  .product-photo {
    position: absolute;
    left: -4px; top: 222px;
    width: 472px; height: 472px;
    border-radius: 50%;
    background: radial-gradient(circle at 50% 48%, #e9c862 0, #f3dc8c 22%, #ffffff 45%, #ffffff 100%);
  }
  .title {
    position: absolute;
    right: 62px; top: 98px;
    font-family: "Great Vibes", cursive;
    font-weight: 400;
    font-size: 96px;
    color: var(--white);
    line-height: 1.1;
  }
  .body-copy {
    position: absolute;
    right: 50px;
    width: 700px;
    text-align: right;
    color: var(--text-gold);
    font-size: 18px;
    line-height: 25.5px;
  }
  .body-copy--first { top: 244px; }
  .body-copy--second { top: 572px; }
  .tagline-banner {
    position: absolute;
    left: 540px; top: 438px;
    width: 700px; height: 90px;
    background: var(--white);
    border-radius: 45px 0 0 45px;
    box-shadow: 0 6px 10px rgba(0, 0, 0, 0.35);
  }
  .tagline-banner::before {
    content: "";
    position: absolute;
    inset: 8px -10px 8px 8px;
    border: 2px dashed #9a6a7e;
    border-radius: 38px 0 0 38px;
  }
  .tagline {
    position: absolute;
    left: 26px; top: 12px;
    white-space: nowrap;
    font-family: "Great Vibes", cursive;
    font-size: 46px;
    color: var(--wine);
  }
</style>
</head>
<body>
<main class="postcard">
  <svg class="shapes" width="1200" height="900" viewBox="0 0 1200 900" aria-hidden="true">
    <defs>
      <linearGradient id="gold-sheen" x1="0" y1="0" x2="1" y2="1">
        <stop offset="0" stop-color="#f7e39a"/>
        <stop offset="0.5" stop-color="#e2bb52"/>
        <stop offset="1" stop-color="#b88a2a"/>
      </linearGradient>
    </defs>
    <path class="sweep" d="M1200 0 L1200 120 C900 190 620 330 520 640 C560 330 820 90 1200 0 Z" fill="rgba(255,255,255,0.06)"/>
    <path class="gold-arc" d="M340 0 C460 300 360 650 700 900" fill="none" stroke="url(#gold-sheen)" stroke-width="13"/>
    <g class="scallop-frame">
      <circle cx="232" cy="458" r="262" fill="url(#gold-sheen)"/>
      <circle cx="232" cy="458" r="262" fill="none" stroke="url(#gold-sheen)" stroke-width="46" stroke-linecap="round" stroke-dasharray="0 54.87"/>
    </g>
  </svg>

  <div class="ornament ornament--top-left" role="img" aria-label="Gold floral swirl ornament"></div>
  <div class="ornament ornament--bottom-left" role="img" aria-label="Gold floral swirl ornament"></div>
  <div class="ornament ornament--top-right" role="img" aria-label="Gold floral corner ornament"></div>
  <div class="ornament ornament--bottom-right" role="img" aria-label="Gold floral corner ornament"></div>

  <div class="product-photo" role="img" aria-label="Photograph of a gold cross pendant on white"></div>

  <h1 class="title">Lorem Ipsum</h1>

  <p class="body-copy body-copy--first">Lorem Ipsum is simply dummy text of the printing and typesetting<br>industry. Lorem Ipsum has been the industry's standard dummy text ever<br>since the 1500s, when an unknown printer took a galley of type and<br>scrambled it to make a type specimen book. It has survived not only five<br>centuries, but also the leap into electronic typesetting, remaining essen-<br>tially unchanged. It was popularised in the 1960s with the release of<br>Letraset sheets containing</p>

  <div class="tagline-banner">
    <p class="tagline">Lorem Ipsum is simply dummy text o</p>
  </div>

  <p class="body-copy body-copy--second">Lorem Ipsum is simply dummy text of the printing and typesetting<br>industry. Lorem Ipsum has been the industry's standard dummy text ever<br>since the 1500s, when an unknown printer took a galley of type and<br>scrambled it to make a type specimen book. It has survived not only five<br>centuries, but also the leap into electronic typesetting, remaining essen-<br>tially unchanged. It was popularised in the 1960s with the release of<br>Letraset sheets containing<br>Lorem Ipsum is simply dummy text of the printing</p>
</main>
</body>
</html>
```